Package Design and Logo - Outdoor Survival Bracelet

Our Company is about to release a new line of high end survival bracelets and we are looking for highly skilled package/logo designers to submit their designs.

Our custom survival bracelets are a trade marked "5 in 1" design that includes a Heavy Duty 15ft Paracord Rope, 18" Tungsten Carbide Finger Saw, Compass, Whistle and a Fire Flint incorporated within the bracelet.
Our brand is called Die Feldlerche and we are looking for a high quality and modern logo in addition to a catchy and visually appealing package design.

We do not have any set styles/designs/content in mind and are very open to any designs, ideas and content you wish to include as long at it keeps a strong outdoors/survival product feel.
Updates

Project Deadline Extended
Reason: Due to many requests, we have decieded to extend the project deadline. Thanks :)

Target Market(s)

Hikers, Backpackers, Travellers, Outdoors, Fishermen, Campers, Skiers, Mountain Bikers.

Requirements
Must have
• Professional and commercial looking design that will be eye catching and gives the appearance of being a high end survival product.
• The logo and package must have a survival, outdoors, wilderness feel about it and
• We are looking for the background of the package to be a HQ image of the ruggered forest with snow covered mountains in the background.

```html
<!DOCTYPE html>
<html lang="en">
<head>
<meta charset="UTF-8">
<title>Die Feldlerche – 5 in 1 Survival Bracelet Package</title>
<link href="https://fonts.googleapis.com/css2?family=Arimo:wght@700&family=Oswald:wght@700&display=swap" rel="stylesheet">
<style>
  :root{
    --canvas:#ffffff;
    --forest:#34460e;
    --sage:#b2b77c;
    --white:#ffffff;
    --cord-light:#e9eadb;
    --cord:#6f7450;
  }
  *{margin:0;padding:0;box-sizing:border-box}
  html,body{width:1200px;height:900px;overflow:hidden;background:var(--canvas)}
  .canvas{position:relative;width:1200px;height:900px}
  .package-art{position:absolute;left:0;top:0}
  .brand{
    position:absolute;left:385px;width:386px;top:196px;text-align:center;
  }
  .brand-name{
    font-family:"Oswald",sans-serif;font-weight:700;font-size:23px;
    letter-spacing:1px;color:var(--forest);line-height:1;text-transform:uppercase;
  }
  .brand-tagline{
    font-family:"Arimo",sans-serif;font-weight:700;font-size:14px;
    color:var(--white);margin-top:3px;line-height:1;
  }
  .product-info{
    position:absolute;left:385px;width:386px;top:596px;text-align:center;
    font-family:"Arimo",sans-serif;font-weight:700;
  }
  .product-count{font-size:30px;color:var(--sage);line-height:1}
  .product-title{font-size:19px;color:var(--white);margin-top:6px;line-height:1}
  .feature-list{font-size:15px;color:var(--sage);margin-top:14px;line-height:23px}
  .feature-list .dot{margin:0 6px}
</style>
</head>
<body>
<main class="canvas">
  <svg class="package-art" width="1200" height="900" viewBox="0 0 1200 900">
    <defs>
      <clipPath id="card-shape">
        <rect x="385" y="111" width="386" height="645" rx="26"/>
      </clipPath>
      <radialGradient id="bracelet-tone" cx="50%" cy="50%" r="50%">
        <stop offset="0%" stop-color="var(--cord-light)"/>
        <stop offset="55%" stop-color="#8d9266"/>
        <stop offset="100%" stop-color="var(--cord-light)"/>
      </radialGradient>
    </defs>
    <g clip-path="url(#card-shape)">
      <rect class="card-base" x="385" y="111" width="386" height="645" fill="var(--forest)"/>
      <path class="top-field" d="M380,455 C430,340 540,320 630,275 C720,230 755,170 775,115 L775,100 L380,100 Z" fill="var(--sage)"/>
      <path class="wave-stripe" d="M380,455 C430,340 540,320 630,275 C720,230 755,170 775,115" fill="none" stroke="var(--white)" stroke-width="9"/>
      <path class="wave-stripe" d="M380,530 C430,420 540,390 640,345 C720,305 760,245 775,205" fill="none" stroke="var(--white)" stroke-width="10"/>
    </g>
    <g class="product-window">
      <ellipse cx="577" cy="518" rx="101" ry="67" fill="var(--white)"/>
      <ellipse cx="577" cy="518" rx="95" ry="61" fill="var(--forest)"/>
      <ellipse cx="577" cy="518" rx="90" ry="56" fill="var(--white)"/>
      <ellipse cx="577" cy="518" rx="86" ry="52" fill="url(#bracelet-tone)" role="img" aria-label="Product photo of an olive paracord survival bracelet with black buckle"/>
    </g>
  </svg>

  <header class="brand">
    <h1 class="brand-name">Die Feldlerche</h1>
    <p class="brand-tagline">survival bracelets</p>
  </header>

  <section class="product-info">
    <p class="product-count">5 in 1</p>
    <h2 class="product-title">survival bracelets</h2>
    <p class="feature-list">
      Paracord Rope <span class="dot">•</span> Finger Saw<br>
      Compass <span class="dot">•</span> Whistle <span class="dot">•</span> Fire Flint
    </p>
  </section>
</main>
</body>
</html>
```